Exercise Physiologist needs business cards

I have a logo, I need business cards (Sole trader) as I am moving to a new location and would like an updated look. I provide gym based exercise rehabilitation, injury prevention and movement assessments. I have over 13 years experience as an Exercise Physiologist. I would like the cards to look professional but not boring and can be a little different to stand out when sitting with other Allied Health Professional cards.

Target Market(s)

GP's, Allied health practitioners, people with injuries wanting to exercise

Industry/Entity Type

Health And Wellness

Contact Information for Business Card

Megan Dorrit - Exercise Physiologist 0437 582 906
14 Larkspur Bend Rd
South Geelong
(Gate 2, Brannock Fitness)
vantorahealth@maildrop-example.com
socialpage-example.com/Vantora

Requirements
Must have
• I would like to include a section to add next appointment date and time space to the back of the card.
Nice to have
• Rounded corners and a black background on 1 or 2 sides.
Should not have
• Pictures of fit/toned bodies etc

```html
<!DOCTYPE html>
<html lang="en">
<head>
<meta charset="utf-8">
<title>Vantora – Business Card</title>
<link rel="stylesheet" href="https://fonts.googleapis.com/css2?family=Arimo:wght@400;700&display=swap">
<style>
  :root {
    --stage: #2b2b2b;
    --card-white: #f7f8fa;
    --card-grey: #e3e6ea;
    --sky: #6cb2e4;
    --sky-deep: #4a93cf;
    --royal: #0d4fae;
    --ink-blue: #1a5fb4;
    --text-white: #ffffff;
  }
  * { margin: 0; padding: 0; box-sizing: border-box; }
  html, body {
    width: 1200px; height: 997px; overflow: hidden;
    background: var(--stage);
    font-family: "Arimo", Arial, sans-serif;
  }
  .stage {
    position: relative; width: 1200px; height: 997px;
  }
  .card {
    position: absolute; top: 348px;
    width: 520px; height: 300px;
    border-radius: 22px; overflow: hidden;
    background: var(--card-white);
    box-shadow: 0 14px 30px rgba(0,0,0,.45);
  }
  .card--back { left: 50px; }
  .card--front { left: 630px; }
  .card__art { position: absolute; inset: 0; }

  /* back: appointment */
  .appointment {
    position: absolute; left: 190px; top: 56px; width: 290px;
    color: var(--ink-blue); text-transform: uppercase;
    font-size: 20px; letter-spacing: .5px;
  }
  .appointment__label { display: block; }
  .appointment__label--date { text-align: center; margin-top: 26px; }
  .appointment__line {
    border-bottom: 2px dashed var(--ink-blue);
    height: 12px; margin-top: 2px;
  }

  /* front: brand */
  .brand {
    position: absolute; right: 34px; top: 78px;
    display: flex; align-items: center; gap: 10px;
  }
  .brand__dot {
    width: 46px; height: 46px; border-radius: 50%;
    border: 4px solid var(--royal);
  }
  .brand__name {
    font-size: 46px; font-weight: 400; color: var(--royal);
    letter-spacing: .5px;
  }

  /* front: person + contact */
  .person { position: absolute; left: 36px; top: 150px; }
  .person__name {
    color: var(--text-white); font-weight: 700; font-size: 21px;
    text-transform: uppercase; letter-spacing: .5px;
  }
  .person__role { color: var(--royal); font-size: 17px; margin-top: 2px; }

  .contact { position: absolute; left: 36px; top: 232px; list-style: none; }
  .contact__item {
    display: flex; align-items: flex-start; gap: 10px;
    color: var(--text-white); font-size: 14px; line-height: 18px;
    margin-bottom: 8px;
  }
  .contact__item--phone { font-size: 16px; font-weight: 400; }
  .contact__item--address { font-weight: 700; font-size: 13px; }
  .contact__icon {
    flex: none; width: 18px; height: 18px; border-radius: 2px;
    background: var(--royal);
  }
</style>
</head>
<body>
<main class="stage">

  <section class="card card--back" aria-label="Card back: next appointment">
    <svg class="card__art" viewBox="0 0 520 300" width="520" height="300" aria-hidden="true">
      <defs>
        <linearGradient id="backWhite" x1="0" y1="0" x2="1" y2="1">
          <stop offset="0" stop-color="#ffffff"/>
          <stop offset="1" stop-color="#e4e7eb"/>
        </linearGradient>
        <linearGradient id="backBlue" x1="0" y1="0" x2="0" y2="1">
          <stop offset="0" stop-color="#6cb2e4"/>
          <stop offset="1" stop-color="#4a93cf"/>
        </linearGradient>
      </defs>
      <rect width="520" height="300" fill="url(#backWhite)"/>
      <path d="M0,170 C110,250 250,292 430,300 L0,300 Z" fill="url(#backBlue)"/>
      <path d="M0,170 C110,250 250,292 430,300" fill="none" stroke="#0d4fae" stroke-width="9"/>
      <circle cx="82" cy="196" r="40" fill="#6cb2e4" stroke="#0d4fae" stroke-width="6"/>
      <circle cx="82" cy="196" r="30" fill="none" stroke="#ffffff" stroke-width="2"/>
    </svg>
    <div class="appointment">
      <span class="appointment__label">Next Appointment</span>
      <div class="appointment__line"></div>
      <span class="appointment__label appointment__label--date">Date &amp; Time</span>
      <div class="appointment__line"></div>
    </div>
  </section>

  <section class="card card--front" aria-label="Card front: contact details">
    <svg class="card__art" viewBox="0 0 520 300" width="520" height="300" aria-hidden="true">
      <defs>
        <linearGradient id="frontBlue" x1="0" y1="0" x2="0" y2="1">
          <stop offset="0" stop-color="#6cb2e4"/>
          <stop offset="1" stop-color="#4a93cf"/>
        </linearGradient>
        <linearGradient id="frontWhite" x1="0" y1="0" x2="1" y2="1">
          <stop offset="0" stop-color="#ffffff"/>
          <stop offset="1" stop-color="#e3e6ea"/>
        </linearGradient>
      </defs>
      <rect width="520" height="300" fill="url(#frontBlue)"/>
      <circle cx="500" cy="40" r="230" fill="url(#frontWhite)" stroke="#0d4fae" stroke-width="10"/>
    </svg>

    <div class="brand">
      <span class="brand__dot"></span>
      <span class="brand__name">vantora</span>
    </div>

    <div class="person">
      <p class="person__name">Megan Dorrit</p>
      <p class="person__role">Exercise Physiologist</p>
    </div>

    <ul class="contact">
      <li class="contact__item contact__item--phone">
        <svg class="contact__icon" viewBox="0 0 18 18" aria-hidden="true">
          <rect width="18" height="18" rx="2" fill="#0d4fae"/>
          <path d="M5 4 L7.5 4 L8.5 7 L7 8 C7.8 9.8 8.2 10.2 10 11 L11 9.5 L14 10.5 L14 13 C9 13.5 4.5 9 5 4 Z" fill="#ffffff"/>
        </svg>
        <span>0437 582 906</span>
      </li>
      <li class="contact__item contact__item--address">
        <svg class="contact__icon" viewBox="0 0 18 18" aria-hidden="true">
          <rect width="18" height="18" rx="2" fill="#0d4fae"/>
          <rect x="3.5" y="5" width="11" height="8" fill="none" stroke="#ffffff" stroke-width="1.3"/>
          <path d="M3.5 5 L9 9.5 L14.5 5" fill="none" stroke="#ffffff" stroke-width="1.3"/>
        </svg>
        <span>14 Larkspur Bend Rd, South Geelong<br>(Gate 2, Brannock Fitness)</span>
      </li>
    </ul>
  </section>

</main>
</body>
</html>
```